VIRTUAL KIDS PARTIES for ages 3-10 years

I need a very urgent leaflet, that looks fun and eye catching aimed at ages 3-10 years.

Award winning, accredited, performing arts provider KVO are excited to bring you LIVE interactive drama, singing and dance parties taught by industry qualified performers that can be accessed from home.

* A chance for your child to hook up with their classmates and friends.

* An interactive hour of games, dancing and singing amongst friends as you talk, laugh and play together on screen.

* Tailor made themes, music choices and routines.

* A chance to socialise in a safe environment and celebrate that special day.

* All staff are qualified, DBS checked industry professionals and teachers.

* Flexible times to suit.

Packages start from £65 plus vat

Visit www.brightmoverstudio.co.uk to book
Check out our online performing arts classes and interactive sessions.

Target Market(s)

Parents and children ages 3-10 years

Colors
ef3f46
ffc214
faa54b
33a6d7
87d0c7
abd037

Requirements
Must have
• Clear text that this is a service for ONLINE VIRTUAL parties

Should be upbeat, happy, bright & vibrant

Logo ( attached)

MUST LOOK PROFESSIONAL

Photo or clever art designs if designer can do this

See attached photos and leaflets for inspiration
Nice to have
• Emphasis on Dance, drama, musical theatre, singing

```html
<!DOCTYPE html>
<html lang="en">
<head>
<meta charset="utf-8">
<title>KVO Online Virtual Parties Leaflet</title>
<link href="https://fonts.googleapis.com/css2?family=Bebas+Neue&family=Kaushan+Script&family=Montserrat:wght@500;600;700&display=swap" rel="stylesheet">
<style>
  :root {
    --red: #ef3f46;
    --yellow: #ffc214;
    --orange: #faa54b;
    --blue: #33a6d7;
    --teal: #87d0c7;
    --lime: #abd037;
    --night: #241338;
    --plum: #3a1d5c;
    --magenta: #7a2a6e;
    --white: #ffffff;
    --page: #e9e9ec;
  }
  * { margin: 0; padding: 0; box-sizing: border-box; }
  html, body { width: 1200px; height: 792px; overflow: hidden; }
  body { background: var(--page); font-family: "Montserrat", sans-serif; position: relative; }

  .leaflet {
    position: absolute; left: 330px; top: 13px; width: 540px; height: 766px; overflow: hidden;
    background:
      radial-gradient(ellipse 320px 220px at 340px 220px, rgba(190, 60, 130, .45), transparent 70%),
      radial-gradient(ellipse 300px 260px at 120px 620px, rgba(110, 50, 170, .35), transparent 70%),
      linear-gradient(180deg, var(--night) 0%, var(--plum) 55%, var(--night) 100%);
    color: var(--white);
  }

  .brand-corner { position: absolute; left: 0; top: 0; width: 140px; height: 145px; }
  .brand-name {
    position: absolute; left: 18px; top: 28px; font-family: "Montserrat", sans-serif;
    font-weight: 700; font-size: 30px; color: var(--red); letter-spacing: 1px;
  }

  .headline {
    position: absolute; left: 140px; top: 12px; width: 384px; text-align: center; white-space: nowrap;
    font-family: "Bebas Neue", sans-serif; font-weight: 400; font-size: 66px; line-height: 1; letter-spacing: 0;
    color: transparent; -webkit-text-stroke: 2.5px var(--yellow);
    text-shadow: 0 0 12px rgba(255, 194, 20, .55);
    transform: scaleY(1.45); transform-origin: top center;
  }

  .title-script {
    position: absolute; left: 18px; top: 140px; font-family: "Kaushan Script", cursive; font-weight: 400;
    font-size: 104px; line-height: 1; color: var(--orange);
    -webkit-text-stroke: 3px var(--red); paint-order: stroke fill;
    text-shadow: 3px 4px 0 var(--red);
  }

  .price-badge { position: absolute; left: 384px; top: 130px; width: 122px; height: 122px; }

  .stripes { position: absolute; left: 0; top: 329px; width: 540px; }
  .stripes span { display: block; height: 16px; margin-bottom: 6px; background: linear-gradient(180deg, #fff, #d9d9e2); }

  .gallery { position: absolute; left: 41px; top: 302px; width: 460px; height: 160px; }
  .gallery .frame { position: absolute; top: 0; width: 101px; height: 154px; }
  .gallery .frame::before {
    content: ""; position: absolute; left: 6px; top: -6px; width: 101px; height: 154px; background: var(--red);
  }
  .gallery .photo {
    position: absolute; inset: 0; border: 4px solid var(--white); box-shadow: 0 2px 6px rgba(0,0,0,.4);
  }
  .photo-one { background: linear-gradient(180deg, #f1eef0, #e46a86 75%, #d8d4d6); }
  .photo-two { background: linear-gradient(180deg, #9fb28b, #efe8e6 55%, #2a2430); }
  .photo-three { background: linear-gradient(180deg, #2a1a12, #e9e1dc 55%, #6c7fb0); }
  .photo-four { background: linear-gradient(180deg, #5a8eb6, #e0a060 45%, #1c1a1e); }

  .features { position: absolute; left: 13px; top: 474px; width: 500px; list-style: none; }
  .features li {
    position: relative; padding-left: 22px; font-size: 12.2px; font-weight: 600; line-height: 13px;
    margin-bottom: 16px;
  }
  .features li svg { position: absolute; left: 0; top: 0; width: 13px; height: 13px; }

  .price-pill {
    position: absolute; left: 199px; top: 633px; width: 327px; height: 24px; border: 1.5px solid var(--white);
    border-radius: 12px; text-align: center; font-weight: 700; font-size: 12.5px; letter-spacing: 1.6px;
    line-height: 21px; white-space: nowrap;
  }

  .web-rule { position: absolute; left: 42px; top: 678px; width: 458px; height: 1.5px; background: var(--white); }
  .web-tag {
    position: absolute; left: 162px; top: 672px; width: 217px; height: 13px; border-radius: 7px;
    background: var(--orange); font-size: 9px; font-weight: 700; letter-spacing: 2px; text-align: center;
    line-height: 13px;
  }
  .web-address {
    position: absolute; left: 0; top: 698px; width: 540px; text-align: center; font-weight: 600;
    font-size: 13.5px; letter-spacing: 2.6px;
  }
  .classes-pill {
    position: absolute; left: 7px; top: 724px; width: 526px; height: 28px; border: 1.5px solid var(--white);
    border-radius: 14px; text-align: center; font-weight: 700; font-size: 11.2px; line-height: 25px; white-space: nowrap;
  }
</style>
</head>
<body>
  <main class="leaflet">
    <svg class="brand-corner" viewBox="0 0 140 145" aria-hidden="true">
      <polygon points="0,0 135,0 106,64 134,115 53,104 0,142" fill="#ffffff"/>
    </svg>
    <div class="brand-name">KVO</div>

    <h1 class="headline">ONLINE VIRTUAL</h1>
    <h2 class="title-script">Parties</h2>

    <svg class="price-badge" viewBox="0 0 122 122" aria-label="Packages start £65">
      <defs>
        <path id="badge-top" d="M22,61 A39,39 0 0 1 100,61"/>
        <path id="badge-bottom" d="M24,66 A37,37 0 0 0 98,66"/>
      </defs>
      <circle cx="61" cy="61" r="59" fill="#1d0f2b"/>
      <circle cx="61" cy="61" r="52" fill="none" stroke="#3a2350" stroke-width="1"/>
      <text font-family="Montserrat, sans-serif" font-weight="700" font-size="13" fill="#ffffff" letter-spacing="3">
        <textPath href="#badge-top" startOffset="50%" text-anchor="middle">PACKAGES</textPath>
      </text>
      <text font-family="Montserrat, sans-serif" font-weight="700" font-size="13" fill="#ffffff" letter-spacing="3" dy="10">
        <textPath href="#badge-bottom" startOffset="50%" text-anchor="middle">START</textPath>
      </text>
      <text x="61" y="70" text-anchor="middle" font-family="Montserrat, sans-serif" font-weight="700" font-size="25" fill="#faa54b" transform="rotate(-18 61 61)">£65</text>
      <circle cx="20" cy="64" r="2.5" fill="#ffc214"/>
      <circle cx="102" cy="64" r="2.5" fill="#ffc214"/>
    </svg>

    <div class="stripes" aria-hidden="true"><span></span><span></span><span></span><span></span></div>

    <div class="gallery">
      <div class="frame" style="left:0"><div class="photo photo-one" role="img" aria-label="Photo of a smiling girl among confetti"></div></div>
      <div class="frame" style="left:116px"><div class="photo photo-two" role="img" aria-label="Photo of a laughing child at a party"></div></div>
      <div class="frame" style="left:232px"><div class="photo photo-three" role="img" aria-label="Photo of a toddler playing in autumn leaves"></div></div>
      <div class="frame" style="left:348px"><div class="photo photo-four" role="img" aria-label="Photo of a girl posing at a fairground"></div></div>
    </div>

    <ul class="features">
      <li><svg viewBox="0 0 13 13"><path d="M1 7 L5 11 L12 1" fill="none" stroke="#33a6d7" stroke-width="2.4" stroke-linecap="round" stroke-linejoin="round"/></svg>A chance for your child to hook up with their classmates and friends</li>
      <li><svg viewBox="0 0 13 13"><path d="M1 7 L5 11 L12 1" fill="none" stroke="#33a6d7" stroke-width="2.4" stroke-linecap="round" stroke-linejoin="round"/></svg>An interactive hour of games, dancing and singing amongst friends as you talk, laugh and play together on screen.</li>
      <li><svg viewBox="0 0 13 13"><path d="M1 7 L5 11 L12 1" fill="none" stroke="#33a6d7" stroke-width="2.4" stroke-linecap="round" stroke-linejoin="round"/></svg>Tailor made themes, music choices and routines.</li>
      <li><svg viewBox="0 0 13 13"><path d="M1 7 L5 11 L12 1" fill="none" stroke="#33a6d7" stroke-width="2.4" stroke-linecap="round" stroke-linejoin="round"/></svg>A chance to socialise in a safe environment and celebrate that special day.</li>
      <li><svg viewBox="0 0 13 13"><path d="M1 7 L5 11 L12 1" fill="none" stroke="#33a6d7" stroke-width="2.4" stroke-linecap="round" stroke-linejoin="round"/></svg>All staff are qualified, DBS checked industry professionals and teachers.</li>
      <li><svg viewBox="0 0 13 13"><path d="M1 7 L5 11 L12 1" fill="none" stroke="#33a6d7" stroke-width="2.4" stroke-linecap="round" stroke-linejoin="round"/></svg>Flexible times to suit.</li>
    </ul>

    <div class="price-pill">PACKAGES START FROM £65 PLUS VAT</div>

    <div class="web-rule"></div>
    <div class="web-tag">VISIT OUR WEBSITE</div>
    <div class="web-address">WWW.BRIGHTMOVERSTUDIO.CO.UK</div>

    <div class="classes-pill">CHECK OUT OUR ONLINE PERFORMING ARTS CLASSES AND INTERACTIVE SESSIONS</div>
  </main>
</body>
</html>
```